Electronic Repair Company need a new flyer!

Hi Guys,

I need a new flyer for my repair company that I can use for my door 2 door marketing. The flyers will be send to thousands of addresses in the Netherlands. You can design the flyer in English but I need to be able to translate the flyer into Dutch, so I might need the PSD file.

We repair Computers, Laptops and ALL Velmora devices.

For some inspiration please take a look at: www.qorvatek.nl

And see the pictures below ;)

Target Market(s)

Computer & Smartphone Repair

Industry/Entity Type

Electronic

Requirements
Nice to have
• I would like to have some pictures from our staff (like on our website) in it so people can see who we really are :)

```html
<!DOCTYPE html>
<html lang="en">
<head>
<meta charset="utf-8">
<title>Qorvatek.nl – Repair Flyer</title>
<link href="https://fonts.googleapis.com/css2?family=Arimo:wght@400;700&family=Michroma&display=swap" rel="stylesheet">
<style>
  :root {
    --orange: #ef4a26;
    --dark: #333333;
    --ink: #222222;
    --white: #ffffff;
    --photo-light: #eeeeee;
    --photo-mid: #d4d4d4;
  }
  html, body { margin: 0; padding: 0; overflow: hidden; }
  body { width: 849px; height: 1200px; background: var(--white); }
  .flyer {
    position: relative; width: 849px; height: 1200px; overflow: hidden;
    background: var(--white); font-family: "Arimo", Arial, sans-serif; color: var(--ink);
  }
  .bar { position: absolute; left: 0; width: 849px; background: var(--orange); }
  .bar--top { top: 0; height: 7px; }
  .bar--bottom { bottom: 0; height: 9px; }

  .brand { position: absolute; left: 41px; top: 44px; display: flex; align-items: center; gap: 10px; }
  .brand__mark { width: 30px; height: 30px; background: var(--orange); }
  .brand__name { font-weight: 700; font-size: 34px; color: var(--ink); letter-spacing: 0.5px; }

  .header-info { position: absolute; right: 41px; top: 36px; text-align: right; font-size: 15.5px; line-height: 19px; }
  .header-info .call { margin-top: 6px; }

  .hero { position: absolute; left: 0; top: 124px; width: 849px; height: 493px; overflow: hidden; }
  .hero__photo { position: absolute; inset: 0; }
  .hero__shapes { position: absolute; inset: 0; }
  .hero__title { position: absolute; right: 41px; top: 50px; text-align: right; color: var(--white); font-family: "Michroma", sans-serif; }
  .hero__title .small { font-size: 34px; line-height: 42px; }
  .hero__title .big { font-size: 58px; line-height: 68px; }
  .hero__promise {
    position: absolute; right: 41px; top: 206px; text-align: right; color: var(--white);
    font-family: "Michroma", sans-serif; font-size: 17px; line-height: 25.6px;
  }
  .hero__promise .accent { color: var(--orange); }
  .hero__slogan {
    position: absolute; left: 41px; top: 340px; color: rgba(255,255,255,0.92);
    font-family: "Michroma", sans-serif; font-size: 29px; line-height: 43px; white-space: nowrap;
  }

  .corner-stripe { position: absolute; left: 0; top: 0; }

  .intro { position: absolute; left: 47px; top: 652px; width: 700px; font-size: 15.5px; line-height: 19px; }
  .intro h2 { margin: 0 0 15px; font-weight: 400; font-size: 19px; line-height: 24px; }
  .intro p { margin: 0 0 5px; white-space: nowrap; }

  .rule { position: absolute; left: 50px; width: 749px; height: 1.5px; background: var(--orange); }
  .rule--one { top: 830px; }
  .rule--two { top: 1097px; }

  .callout { position: absolute; left: 103px; top: 880px; color: var(--orange); }
  .callout .lead { font-size: 17.5px; line-height: 22px; }
  .callout .hours { font-size: 50px; line-height: 54px; margin-bottom: 2px; }
  .callout .q { font-size: 17.5px; line-height: 22px; }
  .callout .phone { font-size: 50px; line-height: 58px; }

  .service { position: absolute; left: 500px; top: 880px; }
  .service h3 { margin: 0; font-weight: 400; font-size: 19.5px; line-height: 22px; }
  .service .sub { font-size: 15.5px; line-height: 19px; margin-bottom: 4px; }
  .service ul { list-style: none; margin: 0; padding: 0; font-size: 15.5px; line-height: 19px; }
  .service li { position: relative; padding-left: 22px; }
  .service li svg { position: absolute; left: 0; top: 7px; }

  .partners {
    position: absolute; left: 36px; right: 36px; top: 1128px; display: flex; justify-content: space-between;
    align-items: center; font-family: "Arimo", sans-serif; font-weight: 700; font-size: 15px;
  }
  .partners span { white-space: nowrap; }
  .p-grey { color: #9a9a9a; font-weight: 400; }
  .p-black { color: #111111; }
  .p-blue { color: #1b4aa8; }
  .p-red { color: #e02a2a; }
  .p-navy { color: #1a2a80; }
  .p-green { color: #82b42b; }
</style>
</head>
<body>
<div class="flyer">
  <div class="bar bar--top"></div>

  <div class="brand">
    <div class="brand__mark"></div>
    <div class="brand__name">QORVATEK.NL</div>
  </div>

  <div class="header-info">
    <div>Binnenkort geopend: Hoorn en Delft Lindenlaan</div>
    <div>58, Utrecht | Molenweg 12, Zuid-Haven</div>
    <div class="call">Call : 088 117 52 30</div>
  </div>

  <section class="hero">
    <svg class="hero__photo" width="849" height="493" role="img" aria-label="Photo of a smiling staff member in an orange and white polo holding an open laptop and a charger cable">
      <defs>
        <linearGradient id="photoTone" x1="0" y1="0" x2="1" y2="0">
          <stop offset="0" stop-color="var(--photo-mid)"/>
          <stop offset="0.5" stop-color="var(--photo-light)"/>
          <stop offset="1" stop-color="var(--photo-mid)"/>
        </linearGradient>
      </defs>
      <rect width="849" height="493" fill="url(#photoTone)"/>
    </svg>
    <svg class="hero__shapes" width="849" height="493" aria-hidden="true">
      <polygon points="342,0 419,0 701,493 624,493" fill="var(--orange)"/>
      <polygon points="419,0 849,0 849,493 701,493" fill="var(--dark)"/>
    </svg>
    <div class="hero__title">
      <div class="small">DO NOT</div>
      <div class="big">PANIC!</div>
    </div>
    <div class="hero__promise">
      <div>WE ENSURE THAT</div>
      <div>YOUR VELMORA</div>
      <div>REPAIRED</div>
      <div>WITHIN</div>
      <div class="accent">24 HOURS</div>
      <div>WITH</div>
      <div class="accent">12 MONTHS</div>
      <div>WARRANTY.</div>
    </div>
    <div class="hero__slogan">
      <div>QUICKLY,</div>
      <div>QUALITATIVELY AND</div>
      <div>ON A NO WIN NO FEE!</div>
    </div>
  </section>

  <svg class="corner-stripe" width="849" height="1200" aria-hidden="true">
    <polygon points="710,624 849,624 849,798 791,798" fill="var(--orange)"/>
  </svg>

  <section class="intro">
    <h2>Pleasant, we Qorvatek.nl</h2>
    <p>More than 20 technicians are six days a week, ready to repair your device as soon as possible.<br>
    Because we have more than 1.2 million parts center in stock, we can often fix within<br>
    24 hours of your device!</p>
    <p>With us you can go for the repair of your Velmora Desk or Velmora Book. Velmora help our<br>
    specialists will be happy with a professional repair.</p>
  </section>

  <div class="rule rule--one"></div>

  <section class="callout">
    <div class="lead">Your device repaired within</div>
    <div class="hours">24 hours!</div>
    <div class="q">Do you have a question?</div>
    <div class="q">Call our customer service</div>
    <div class="phone">088-1175230</div>
  </section>

  <section class="service">
    <h3>GENUINE SERVICE</h3>
    <div class="sub">We do nothing else!</div>
    <ul>
      <li><svg width="16" height="10" viewBox="0 0 16 10"><path d="M1 6 L5 9 L15 1" fill="none" stroke="var(--orange)" stroke-width="1.5"/></svg>Repair within 24 hours</li>
      <li><svg width="16" height="10" viewBox="0 0 16 10"><path d="M1 6 L5 9 L15 1" fill="none" stroke="var(--orange)" stroke-width="1.5"/></svg>Smartphones within 30 minutes</li>
      <li><svg width="16" height="10" viewBox="0 0 16 10"><path d="M1 6 L5 9 L15 1" fill="none" stroke="var(--orange)" stroke-width="1.5"/></svg>12 month warranty</li>
      <li><svg width="16" height="10" viewBox="0 0 16 10"><path d="M1 6 L5 9 L15 1" fill="none" stroke="var(--orange)" stroke-width="1.5"/></svg>Passing by without an<br>appointment</li>
      <li><svg width="16" height="10" viewBox="0 0 16 10"><path d="M1 6 L5 9 L15 1" fill="none" stroke="var(--orange)" stroke-width="1.5"/></svg>Free &amp; insured&nbsp; shipping</li>
      <li><svg width="16" height="10" viewBox="0 0 16 10"><path d="M1 6 L5 9 L15 1" fill="none" stroke="var(--orange)" stroke-width="1.5"/></svg>No cure no pay!</li>
    </ul>
  </section>

  <div class="rule rule--two"></div>

  <div class="partners">
    <span class="p-grey">Velmora</span>
    <span class="p-black">Sonrel</span>
    <span class="p-blue">Kavo</span>
    <span class="p-blue">Marendo</span>
    <span class="p-red">Tarvik</span>
    <span class="p-red">Vorelta</span>
    <span class="p-blue">Orbix</span>
    <span class="p-navy">Zentra</span>
    <span class="p-blue">Delvo</span>
    <span class="p-green">Lumio</span>
  </div>

  <div class="bar bar--bottom"></div>
</div>
</body>
</html>
```